VoIP Postcard - New customer prospects

Need a postcard that gets our brand in front of the locals. We are an established IT company that has been in business for 20 years. We need to put a campaign in front of local businesses to let then know what we do. You can see our info at larkvoice.net. We currently do not have a logo for our branded LarkVoice VoIP service, which is part of Brindlewood Data Works.

Target Market(s)

Business Owners

Industry/Entity Type

Business

Colors
0355a3
3276b5
33a6d7
ec1f27
f04a50

```html
<!DOCTYPE html>
<html lang="en">
<head>
<meta charset="utf-8">
<title>LarkVoice Postcard</title>
<link rel="stylesheet" href="https://fonts.googleapis.com/css2?family=Raleway:wght@300;400&family=Roboto+Condensed:wght@400;700&display=swap">
<style>
  :root{
    --navy:#0a2f6b;
    --blue:#0355a3;
    --mid-blue:#3276b5;
    --sky:#33a6d7;
    --red:#ec1f27;
    --soft-red:#f04a50;
    --deep-red:#a5101c;
    --ink:#1d1d1d;
    --white:#ffffff;
    --grey:#8e8e8e;
    --line:#6f6f6f;
  }
  *{box-sizing:border-box;margin:0;padding:0}
  html,body{width:870px;height:1200px;overflow:hidden}
  body{
    position:relative;
    background:radial-gradient(ellipse at 50% 48%,#f2f2f2 0%,#cfcfcf 55%,#9a9a9a 100%);
    font-family:"Roboto Condensed",Arial,sans-serif;
    color:var(--ink);
  }
  .card{position:absolute;left:105px;width:641px;height:494px;overflow:hidden;background:var(--white);box-shadow:0 4px 10px rgba(0,0,0,.35)}
  .card--front{top:41px}
  .card--back{top:633px;height:493px}
  .side-label{position:absolute;left:0;width:870px;text-align:center;font-family:"Roboto Condensed",sans-serif;font-weight:700;font-size:32px;color:#5c5c5c}
  .side-label--front{top:572px}
  .side-label--back{top:1148px}

  /* front */
  .front-photo{position:absolute;left:0;top:0;width:641px;height:246px;
    background:linear-gradient(180deg,#e8e6d6 0%,#b9c3d8 20%,#6f7fb8 42%,#4a5690 65%,#5a6275 100%)}
  .front-title{position:absolute;top:74px;width:100%;text-align:center;font-family:"Raleway",sans-serif;font-weight:400;font-size:36px;color:var(--white);text-shadow:0 2px 3px rgba(0,0,0,.5)}
  .front-sub{position:absolute;top:120px;width:100%;text-align:center;font-size:17px;color:var(--white);text-shadow:0 1px 2px rgba(0,0,0,.6)}
  .band{position:absolute;top:257px;height:174px;width:641px;background:linear-gradient(90deg,var(--navy),var(--mid-blue) 30%,var(--navy) 50%,var(--mid-blue) 70%,var(--navy))}
  .feature{position:absolute;top:269px;width:177px;height:150px;background:var(--white);text-align:center}
  .feature--products{left:13px}
  .feature--contact{left:453px}
  .feature h3{font-size:14.5px;font-weight:700;color:var(--red);margin-top:6px}
  .feature p{font-size:11px;line-height:13px;margin-top:4px;color:var(--ink)}
  .feature svg{display:block;margin:12px auto 0}
  .center-panel{position:absolute;left:186px;top:169px;width:269px;height:262px;background:var(--white)}
  .chart-frame{position:absolute;left:196px;top:179px;width:249px;height:190px;background:var(--deep-red);padding:8px;box-shadow:0 3px 6px rgba(0,0,0,.3)}
  .chart-inner{width:100%;height:100%;background:var(--white);text-align:center}
  .chart-inner svg{display:block;margin:0 auto}
  .chart-inner h3{font-size:14.5px;font-weight:700;color:var(--red);margin-top:2px}
  .chart-inner p{font-size:11px;line-height:13px;margin-top:4px}
  .brand{display:flex;align-items:center;gap:6px;position:absolute}
  .brand__name{font-family:"Roboto Condensed",sans-serif;font-weight:700;font-size:15px;color:var(--blue);white-space:nowrap}
  .brand__dot{width:22px;height:22px;border-radius:50%;background:var(--red);flex:none}
  .front-brand{left:240px;top:442px}
  .stripe{position:absolute;bottom:0;height:7px}
  .stripe--blue{left:0;width:457px;background:var(--blue)}
  .stripe--red{left:461px;right:0;background:var(--red)}

  /* back */
  .back-photo{position:absolute;left:0;top:0;width:367px;height:173px;background:linear-gradient(180deg,#16367a 0%,#2450a0 45%,#1b3a6e 75%,#2e4d50 100%)}
  .back-scenery{position:absolute;left:0;top:173px;width:641px;height:320px;background:linear-gradient(180deg,#e6e6e6 0%,#d2d2d2 60%,#bdbdbd 100%)}
  .back-scenery--right{left:367px;top:0;width:274px;height:493px;background:linear-gradient(180deg,#f0f0f0 0%,#dcdcdc 50%,#b8b8b8 100%)}
  .back-title{position:absolute;left:0;top:14px;width:367px;text-align:center;font-family:"Raleway",sans-serif;font-weight:400;font-size:24px;line-height:26px;color:var(--white)}
  .back-intro{position:absolute;left:0;top:78px;width:367px;text-align:center;font-size:14.5px;line-height:20px;color:var(--white)}
  .logo-box{position:absolute;left:66px;top:130px;width:235px;height:112px;background:var(--white);padding:5px;box-shadow:0 2px 4px rgba(0,0,0,.3)}
  .logo-box__inner{position:relative;width:100%;height:100%;background:linear-gradient(180deg,var(--mid-blue),var(--blue))}
  .logo-box .brand{left:22px;top:40px}
  .logo-box .brand__name{color:var(--white)}
  .features-list{position:absolute;left:78px;top:268px;list-style:none}
  .features-list li{position:relative;padding-left:20px;font-size:14px;height:29.3px;line-height:20px}
  .features-list li::before{content:"";position:absolute;left:0;top:4px;width:12px;height:12px;border-radius:50%;background:var(--mid-blue)}
  .features-list li:nth-child(even)::before{background:var(--red)}
  .contact-band{position:absolute;left:0;top:415px;width:367px;height:78px;background:var(--mid-blue);color:var(--white);text-align:center;font-size:16.5px;line-height:20px;padding-top:26px}
  .contact-tab{position:absolute;left:91px;top:400px;width:170px;height:0;border-bottom:29px solid var(--navy);border-left:22px solid transparent;border-right:22px solid transparent}
  .contact-tab span{position:absolute;left:-22px;width:170px;top:4px;text-align:center;font-size:16px;font-weight:700;color:var(--white)}
  .stamp{position:absolute;left:528px;top:50px;width:91px;height:102px;border:2px solid var(--line)}
  .address-line{position:absolute;left:381px;width:238px;height:1.5px;background:var(--line)}
  .site-note{position:absolute;left:367px;width:274px;top:436px;text-align:center;font-size:14px;color:var(--ink)}
  .site-url{position:absolute;left:367px;width:274px;top:453px;text-align:center;font-family:"Raleway",sans-serif;font-weight:300;font-size:25px;color:var(--mid-blue)}
</style>
</head>
<body>

<section class="card card--front">
  <div class="front-photo" role="img" aria-label="Mountain valley landscape at sunrise with blue peaks and clouds"></div>
  <h1 class="front-title">Welcome to LarkVoice</h1>
  <p class="front-sub">Enjoy peace of mind and relax knowing your phones work for you</p>

  <div class="band"></div>

  <article class="feature feature--products">
    <svg width="84" height="58" viewBox="0 0 84 58" aria-hidden="true">
      <path d="M14 44 L30 14 L74 14 L80 44 Z" fill="#2b2f36"/>
      <rect x="48" y="18" width="22" height="10" fill="#9fb3c8"/>
      <g fill="#d6d6d6">
        <rect x="40" y="32" width="5" height="3"/><rect x="48" y="32" width="5" height="3"/><rect x="56" y="32" width="5" height="3"/>
        <rect x="40" y="37" width="5" height="3"/><rect x="48" y="37" width="5" height="3"/><rect x="56" y="37" width="5" height="3"/>
      </g>
      <path d="M4 46 Q6 38 16 40 L30 14 Q24 6 18 12 L2 42 Z" fill="#1c1f24"/>
      <rect x="12" y="44" width="70" height="6" rx="2" fill="#1c1f24"/>
    </svg>
    <h3>Discover our phone products</h3>
    <p>We have many models of phones<br>to review, and more on the way.<br>Find out more!</p>
  </article>

  <div class="center-panel"></div>
  <div class="chart-frame">
    <div class="chart-inner">
      <svg class="growth-chart" width="200" height="112" viewBox="0 0 200 112" aria-hidden="true">
        <line x1="40" y1="100" x2="168" y2="100" stroke="#9a9a9a" stroke-width="1.5"/>
        <line x1="40" y1="100" x2="40" y2="18" stroke="#9a9a9a" stroke-width="1.5"/>
        <rect x="52" y="78" width="18" height="22" fill="#3276b5"/>
        <rect x="80" y="64" width="18" height="36" fill="#3276b5"/>
        <rect x="108" y="48" width="18" height="52" fill="#0355a3"/>
        <rect x="136" y="26" width="18" height="74" fill="#ec1f27"/>
      </svg>
      <h3>Our service beats all the rest</h3>
      <p>Our product and service is completely<br>off the charts! Find out why!</p>
    </div>
  </div>

  <article class="feature feature--contact">
    <svg width="90" height="58" viewBox="0 0 90 58" aria-hidden="true">
      <path d="M22 22 Q45 8 68 22 L64 30 L56 28 L56 22 Q45 18 34 22 L34 28 L26 30 Z" fill="#1f5f7a"/>
      <path d="M30 30 L60 30 L68 52 L22 52 Z" fill="#2a7896"/>
      <circle cx="45" cy="41" r="7" fill="#fff"/>
      <circle cx="45" cy="41" r="3" fill="#2a7896"/>
      <circle cx="12" cy="22" r="7" fill="#f6b11c"/>
      <circle cx="80" cy="20" r="6" fill="#f6b11c"/>
      <circle cx="30" cy="6" r="5" fill="#1f5f7a"/>
      <circle cx="62" cy="6" r="5" fill="#fff" stroke="#1f5f7a" stroke-width="1.5"/>
    </svg>
    <h3>Contact us</h3>
    <p>To find out more about our products<br>and services, contact us!</p>
  </article>

  <div class="brand front-brand">
    <span class="brand__name">Brindlewood Data Works</span>
    <span class="brand__dot"></span>
  </div>

  <div class="stripe stripe--blue"></div>
  <div class="stripe stripe--red"></div>
</section>
<p class="side-label side-label--front">front</p>

<section class="card card--back">
  <div class="back-scenery" role="img" aria-label="Faded grey rocky hillside"></div>
  <div class="back-scenery back-scenery--right" role="img" aria-label="Faded grey rock formation under a cloudy sky"></div>
  <div class="back-photo" role="img" aria-label="Blue-toned mountain range under a dusky sky"></div>

  <h2 class="back-title">Learn more<br>about our features</h2>
  <p class="back-intro">Our phone service provides many great features!<br>Jump on in and find out more!</p>

  <div class="logo-box">
    <div class="logo-box__inner">
      <div class="brand">
        <span class="brand__name">Brindlewood Data Works</span>
        <span class="brand__dot"></span>
      </div>
    </div>
  </div>

  <ul class="features-list">
    <li>Lorem Ipsum is simply dummy text.</li>
    <li>Lorem Ipsum is simply dummy text.</li>
    <li>Lorem Ipsum is simply dummy text.</li>
    <li>Lorem Ipsum is simply dummy text.</li>
  </ul>

  <div class="contact-band">
    address goes to here.<br>
    Phone : 0123 456 789 &nbsp;|&nbsp; email : hello@larkvoice.net
  </div>
  <div class="contact-tab"><span>GET IN TOUCH</span></div>

  <div class="stamp"></div>
  <div class="address-line" style="top:190px"></div>
  <div class="address-line" style="top:237px"></div>
  <div class="address-line" style="top:282px"></div>
  <div class="address-line" style="top:328px"></div>
  <div class="address-line" style="top:378px"></div>

  <p class="site-note">You can see our info at :</p>
  <p class="site-url">larkvoice.net</p>
</section>
<p class="side-label side-label--back">back</p>

</body>
</html>
```